Velmora Partners - website for real estate investment company

Create a bold, modern website that reflects Velmora’s success, professionalism, and credibility.
The design must stand out while maintaining a polished, corporate tone. (bold, but understated)
The client just created a new logo, and the website design must be in sync with the logo design. Information about the logo colors, fonts, and message are in the attached design brief.
Updates

Target Market(s)

b2b: banks, brokers, institutional partners, vendors, and property sellers.

Industry/Entity Type

real estate investment company

Number of Pages Required

1 page

Font styles to use
Sans Serif

Colors

Designer to choose colors to be used in the design.

Requirements
Must have
• 1. homepage design (psd) 2. a top banner image (psd) for a default inner page
Nice to have
• please see attached design brief
Should not have

```html
<!DOCTYPE html>
<html lang="en">
<head>
<meta charset="UTF-8">
<title>Velmora Partners</title>
<link href="https://fonts.googleapis.com/css2?family=Lexend:wght@300;400;500;600;700&display=swap" rel="stylesheet">
<style>
:root{
  --navy:#0f2c56;
  --ink:#16163a;
  --red:#e11f2a;
  --red-soft:#f08a8f;
  --pink:#fde8ea;
  --blush:#fff5f6;
  --grey:#6b6b7b;
  --line:#d9d9e0;
  --white:#ffffff;
  --map:#eceef1;
}
*{margin:0;padding:0;box-sizing:border-box}
html,body{width:1200px;height:3206px;overflow:hidden}
body{font-family:"Lexend",sans-serif;color:var(--ink);background:var(--white);position:relative}
.abs{position:absolute}
.photo{position:absolute}

/* header + hero */
.hero{left:0;top:0;width:1200px;height:525px}
.hero .photo{inset:0;background:linear-gradient(180deg,#5f9ad6 0%,#88b6dd 18%,#3f5f86 38%,#56677a 52%,#6e7884 75%,#8a929b 100%)}
.hero-cut{position:absolute;left:0;top:470px}
.topbar{left:0;top:0;width:1200px;height:55px;background:linear-gradient(180deg,rgba(20,70,150,.9),rgba(30,90,170,.55))}
.brand{left:187px;top:12px;font-size:27px;font-weight:700;color:var(--white);letter-spacing:.5px}
.nav{right:188px;top:20px;display:flex;gap:19px;font-size:11.5px;font-weight:500;color:var(--white)}
.nav .on{color:var(--red);border-bottom:2px solid var(--red);padding-bottom:4px}
.hero-title{left:0;width:1200px;top:305px;text-align:center;font-size:52px;font-weight:700;color:var(--white);letter-spacing:-.5px}
.hero-sub{left:200px;width:800px;top:380px;text-align:center;font-size:11px;font-weight:500;color:var(--white);line-height:16px}
.play{left:565px;top:460px;width:70px;height:70px;border-radius:50%;background:var(--red);color:var(--white);font-size:13px;font-weight:500;display:flex;align-items:center;justify-content:center;box-shadow:0 6px 18px rgba(225,31,42,.35)}
.play::after{content:"";position:absolute;inset:6px;border:1.5px dashed rgba(255,255,255,.8);border-radius:50%}

/* stats */
.stat{top:593px;height:84px;background:var(--white);box-shadow:0 4px 18px rgba(0,0,0,.07);padding:12px 13px;font-size:15px;font-weight:500}
.stat svg{display:block;margin-bottom:10px}
.stat.hl{background:var(--pink)}

/* key */
.img-a{left:187px;top:758px;width:217px;height:172px;background:linear-gradient(135deg,#cfd6db,#7d8a94)}
.img-b{left:403px;top:746px;width:158px;height:196px;background:linear-gradient(180deg,#d9b88a,#5f7a93 60%,#3b4652)}
.img-c{left:293px;top:785px;width:158px;height:187px;background:linear-gradient(180deg,#c3d4e6,#6e8396 60%,#3d4c3a);border:2px solid var(--white)}
.key-h{left:612px;top:738px;width:400px;font-size:25px;font-weight:600;line-height:30px}
.key-p{left:632px;top:817px;width:382px;font-size:11.2px;font-weight:300;line-height:16.3px;color:#45455a}
.key-line{left:615px;top:818px}

/* strategy */
.section-bg{left:0;top:1020px;width:1200px;height:900px;background:linear-gradient(180deg,#fff 0%,var(--blush) 40%,#fff 100%)}
.h2{left:0;width:1200px;text-align:center;font-size:31px;font-weight:600}
.acc{left:187px;top:1128px;width:460px}
.acc-item{border-bottom:1px solid var(--line);padding:14px 0 15px;font-size:18.5px;font-weight:500}
.acc-item:first-child{padding-top:0}
.acc-item p{font-size:11.2px;font-weight:300;line-height:16px;color:#4a4a5c;margin-top:8px}
.strat-img{left:703px;top:1116px;width:310px;height:275px;background:linear-gradient(180deg,#8b9099 0%,#c9a57a 38%,#5c6470 60%,#3a4049 100%)}

/* benefits */
.card{top:1535px;width:263px;background:var(--white);box-shadow:0 4px 18px rgba(0,0,0,.06);padding:22px 19px}
.card h3{font-size:19px;font-weight:500;line-height:24px;margin:14px 0 14px}
.card p{font-size:11.2px;font-weight:300;line-height:16px;color:#4a4a5c}
.btn{background:var(--red);color:var(--white);font-size:11px;font-weight:500;border-radius:3px;text-align:center}

/* band */
.band{left:0;top:1880px;width:1200px;height:500px}
.band-h{left:0;width:1200px;top:2043px;text-align:center;font-size:31px;font-weight:600;color:var(--white);line-height:36px}
.contact{left:0;width:1200px;top:2138px;display:flex;justify-content:center;gap:30px;font-size:19px;font-weight:500;color:var(--white)}
.contact span{display:flex;align-items:center;gap:14px}
.ic{width:30px;height:30px;border-radius:50%;background:var(--white);display:flex;align-items:center;justify-content:center}

/* portfolio */
.prop{top:2502px;width:192px;height:188px;background:var(--white);box-shadow:0 4px 16px rgba(0,0,0,.08);padding:6px}
.prop .photo{position:relative;height:108px;background:linear-gradient(180deg,#b8c6d3 0%,#9aa5ae 45%,#7c8a70 80%,#5f6d50 100%)}
.meta{display:flex;gap:10px;font-size:8px;color:#777;margin:13px 0 0 3px}
.meta b{font-weight:400;color:var(--red)}
.prop h4{font-size:12.5px;font-weight:500;margin:9px 0 0 3px}
.arrow{top:2582px;font-size:16px;color:var(--ink)}

/* contact form */
.map{left:0;top:2830px;width:1200px;height:330px;background:var(--map)}
.form{left:242px;top:2757px;width:716px;height:270px;background:var(--white);border:1px solid #d0d0d8}
.form h2{position:absolute;top:32px;width:100%;text-align:center;font-size:29px;font-weight:600}
.form .lead{position:absolute;top:78px;width:100%;text-align:center;font-size:11px;font-weight:300;color:#444}
.field{position:absolute;width:313px;height:37px;border:1px solid #b9b9c4;font-size:10px;color:#666;padding:12px 9px}
.check{position:absolute;left:37px;top:216px;display:flex;align-items:center;gap:8px;font-size:11px}
.check i{width:15px;height:15px;border:1px solid #999;border-radius:2px}
.check a{color:var(--red)}
.up{left:593px;top:3076px;width:44px;height:44px;border-radius:50%;border:1.5px solid var(--navy);background:var(--white);display:flex;align-items:center;justify-content:center}

/* footer */
.footer{left:0;top:3160px;width:1200px;height:46px;background:var(--navy);color:var(--white);font-size:11px}
.footer .links{position:absolute;left:187px;top:19px;display:flex;gap:20px}
.footer .copy{position:absolute;right:187px;top:19px}
.follow{left:522px;top:3138px;width:194px;height:38px;border-radius:20px;background:var(--white);border:1.5px solid var(--navy);display:flex;align-items:center;justify-content:center;gap:12px;font-size:10px;color:var(--ink)}
.social{width:16px;height:16px;border-radius:50%;background:var(--navy)}
</style>
</head>
<body>

<section class="hero abs">
  <div class="photo" role="img" aria-label="City skyline with skyscrapers and a cable bridge above a paved plaza"></div>
  <svg class="hero-cut" width="1200" height="60" viewBox="0 0 1200 60">
    <polygon points="0,12 1200,50 1200,60 0,60" fill="#fff"/>
    <polygon points="0,10 1200,46 1200,52 0,14" fill="#f6b8bb"/>
  </svg>
  <div class="topbar abs"></div>
  <div class="brand abs">VELMORA</div>
  <nav class="nav abs"><span class="on">Home</span><span>Our Story</span><span>Investment Strategy</span><span>What Sets Us Apart</span><span>Our Portfolio</span><span>Contact</span></nav>
  <h1 class="hero-title abs">Experience – Strategy – Vision</h1>
  <p class="hero-sub abs">Velmora Partners Is A Vertically Integrated Real Estate Investment Firm With A Proven Four-Decade Track Record. We Acquire, Reposition, And Operate High-Performing Assets Across Multiple Sectors — Always With A Focus On Exceptional, Risk-Adjusted Returns.</p>
</section>
<div class="play abs">Play</div>

<div class="stat abs" style="left:187px;width:323px">
  <svg width="26" height="26" viewBox="0 0 26 26" fill="none" stroke="#16163a" stroke-width="1.3"><rect x="4" y="8" width="10" height="16"/><rect x="14" y="3" width="8" height="21"/><path d="M7 12h4M7 16h4M7 20h4M17 7h2M17 11h2M17 15h2"/></svg>
  23,000+ multifamily &amp; healthcare units
</div>
<div class="stat hl abs" style="left:535px;width:137px">
  <svg width="26" height="26" viewBox="0 0 26 26" fill="none" stroke="#16163a" stroke-width="1.3"><rect x="5" y="2" width="16" height="22"/><path d="M9 6h8M9 10h8M9 14h8M9 18h8"/></svg>
  Founded: 1989
</div>
<div class="stat abs" style="left:695px;width:318px">
  <svg width="30" height="26" viewBox="0 0 30 26" fill="none" stroke="#16163a" stroke-width="1.3"><circle cx="15" cy="8" r="6"/><path d="M15 5v6M2 20l6-4h8l-3 3h6l6-4"/><path d="M2 24h20"/></svg>
  $300+ million invested in renovations
</div>

<div class="section-bg abs"></div>

<div class="photo img-a" role="img" aria-label="Business team meeting in a bright office"></div>
<div class="photo img-b" role="img" aria-label="Aerial city view at sunset"></div>
<div class="photo img-c" role="img" aria-label="Modern glass office tower"></div>
<h2 class="key-h abs">The Key to Our Investment Success</h2>
<svg class="key-line abs" width="6" height="164" viewBox="0 0 6 164"><line x1="3" y1="0" x2="3" y2="158" stroke="#e11f2a" stroke-width="1"/><polygon points="0,157 6,157 3,163" fill="#e11f2a"/></svg>
<p class="key-p abs">Hope Island's real estate market continues to demonstrate strong resilience, particularly in its premium waterfront and lifestyle segments. According to Parcelwise data via Property Ledger Magazine, the current median house price stands at approximately AUD 1.85 million, with an annual capital growth rate of 0.00%, and houses now spend an average of 57 days on market. Rental yields hold steady at around 3.72%, supported by a median weekly rent of AUD 1,150. Notably, while quarterly house values have declined by about –3.65%, the 12-month trend remains flat, reflecting a stable yet cautious market environment In contrast,...</p>

<h2 class="h2 abs" style="top:1048px">Our Complete Investment Strategy</h2>
<div class="acc abs">
  <div class="acc-item">Quantitative Review<p>Everyone likes to know what's happening in the property market in their suburb. One of the foundations of understanding your property's value is knowing what sale prices have recently been achieved.</p></div>
  <div class="acc-item">Due Diligence</div>
  <div class="acc-item">Plan Development</div>
  <div class="acc-item">Reposition For Returns</div>
</div>
<div class="photo strat-img" role="img" aria-label="City skyline at sunset under dramatic clouds"></div>

<h2 class="h2 abs" style="top:1463px">Explore A Brighter Way</h2>
<div class="card abs" style="left:187px">
  <svg width="46" height="40" viewBox="0 0 46 40" fill="none" stroke="#e11f2a" stroke-width="1.6"><rect x="4" y="20" width="7" height="14"/><rect x="15" y="12" width="7" height="22"/><rect x="26" y="6" width="7" height="28"/><path d="M2 37h34"/><text x="36" y="30" font-size="13" fill="#e11f2a" stroke="none" font-family="Lexend">$</text></svg>
  <h3>Appreciation of Value</h3>
  <p>Reliable income from real estate investments can potentially make a greater return comparative to markets, with less volatility.</p>
</div>
<div class="card abs" style="left:469px">
  <svg width="40" height="40" viewBox="0 0 40 40" fill="none" stroke="#e11f2a" stroke-width="1.6"><path d="M14 26c4-12 12-20 22-22-2 10-10 18-22 22z"/><circle cx="26" cy="14" r="3"/><path d="M14 26l-6-2 6-8h6M14 26l2 6 8-6v-6M10 30l-6 6"/></svg>
  <h3>Potential Inflation Hedge</h3>
  <p>Reliable income from real estate investments can potentially make a greater return comparative to markets, with less volatility.</p>
</div>
<div class="card abs" style="left:750px">
  <svg width="42" height="44" viewBox="0 0 42 44" fill="none" stroke="#e11f2a" stroke-width="1.6"><path d="M4 2h34v40l-5-3-6 3-6-3-6 3-6-3-5 3z"/><path d="M15 18l12-10"/><circle cx="15" cy="9" r="2.5"/><circle cx="27" cy="17" r="2.5"/><path d="M11 26h20M11 32h20"/></svg>
  <h3>Tax Efficiency</h3>
  <p>The ability to use depreciation and other write-offs can create powerful tax benefits and enable investors to enhance their after-tax returns.</p>
</div>
<div class="btn abs" style="left:557px;top:1804px;width:86px;height:26px;line-height:26px">Learn More</div>

<svg class="band abs" width="1200" height="500" viewBox="0 0 1200 500">
  <defs><linearGradient id="bandfill" x1="0" y1="0" x2="0" y2="1"><stop offset="0" stop-color="#0f2c56"/><stop offset="1" stop-color="#1b3a66"/></linearGradient></defs>
  <polygon points="0,12 1200,72 1200,80 0,22" fill="#f08a8f"/>
  <polygon points="0,0 1200,60 1200,74 0,14" fill="#e94c55"/>
  <polygon points="0,22 1200,80 1200,440 0,420" fill="url(#bandfill)"/>
  <polygon points="0,420 1200,440 1200,492 0,428" fill="#f08a8f"/>
  <polygon points="0,418 1200,438 1200,452 0,422" fill="#e94c55"/>
</svg>
<div class="photo abs" style="left:420px;top:1950px;width:360px;height:360px;background:radial-gradient(ellipse at 50% 40%,rgba(80,110,150,.45),rgba(15,44,86,0) 70%)" role="img" aria-label="Glass tower over a dotted world map with dollar coins"></div>
<h2 class="band-h abs">Velmora is one of the largest privately held real<br>estate investors and managers in the world.</h2>
<div class="contact abs">
  <span><i class="ic"><svg width="14" height="18" viewBox="0 0 14 18"><path d="M7 0a7 7 0 0 0-7 7c0 5 7 11 7 11s7-6 7-11a7 7 0 0 0-7-7z" fill="#e11f2a"/><circle cx="7" cy="7" r="2.5" fill="#fff"/></svg></i>Ashford, NJ</span>
  <span><i class="ic"><svg width="16" height="12" viewBox="0 0 16 12" fill="none" stroke="#e11f2a" stroke-width="1.5"><rect x="1" y="1" width="14" height="10"/><path d="M1 1l7 6 7-6"/></svg></i>info@velmora.com</span>
</div>
<div class="btn abs" style="left:544px;top:2190px;width:112px;height:25px;line-height:25px">Career Inquiries</div>

<h2 class="h2 abs" style="top:2430px">Our Real Estate Portfolio</h2>
<div class="arrow abs" style="left:164px">‹</div>
<div class="arrow abs" style="left:1026px">›</div>
<div class="prop abs" style="left:187px"><div class="photo" role="img" aria-label="Suburban two-storey house with garage"></div><div class="meta"><span><b>⊖</b> Active</span><span><b>▢</b> 328</span><span><b>⌖</b> Dallas, TX</span></div><h4>Marlow Apartments</h4></div>
<div class="prop abs" style="left:398px"><div class="photo" role="img" aria-label="White family home with lawn"></div><div class="meta"><span><b>⊖</b> Active</span><span><b>▢</b> 328</span><span><b>⌖</b> Dallas, TX</span></div><h4>Ridges at Fernvale</h4></div>
<div class="prop abs" style="left:609px"><div class="photo" role="img" aria-label="Modern stone and wood house"></div><div class="meta"><span><b>⊖</b> Active</span><span><b>▢</b> 328</span><span><b>⌖</b> Dallas, TX</span></div><h4>Harbor Apartments</h4></div>
<div class="prop abs" style="left:820px"><div class="photo" role="img" aria-label="Townhouse with orange garage door"></div><div class="meta"><span><b>⊖</b> Active</span><span><b>▢</b> 328</span><span><b>⌖</b> Dallas, TX</span></div><h4>Linden Townhomes</h4></div>

<div class="map abs" role="img" aria-label="Faint world map background"></div>
<div class="form abs">
  <h2>GET IN TOUCH</h2>
  <p class="lead">Let's connect to explore how we can help your business grow with clarity and confidence.</p>
  <div class="field" style="left:37px;top:107px">Name</div>
  <div class="field" style="left:365px;top:107px">Last Name</div>
  <div class="field" style="left:37px;top:160px">Email Address</div>
  <div class="field" style="left:365px;top:160px">Phone Number</div>
  <div class="check"><i></i>I Accept <a>Terms &amp; Conditions</a></div>
  <div class="btn" style="position:absolute;left:584px;top:213px;width:94px;height:25px;line-height:25px">Submit Now</div>
</div>
<div class="up abs"><svg width="14" height="16" viewBox="0 0 14 16" fill="none" stroke="#0f2c56" stroke-width="1.6"><path d="M7 15V2M1 8l6-6 6 6"/></svg></div>

<footer class="footer abs">
  <div class="links"><span>Privacy Policy</span><span>Terms &amp; Conditions</span></div>
  <div class="copy">© 2025 Velmora Partners</div>
</footer>
<div class="follow abs">Follow Us <i class="social" aria-label="Social link"></i><i class="social" aria-label="Social link"></i><i class="social" aria-label="Social link"></i></div>

</body>
</html>
```